Company Employee Onboarding Presentation

We need a custom PowerPoint design for a company presentation. This presentation will be sent to new employees during their onboarding/hiring process. We have attached a current mock-up of the presentation - but this is for content only. We do not like the style of the mock-up. We're a commercial real estate investment company based in Los Angeles, CA. Our website is: www.thequillmrk.com.

One artistic element that we want in the presentation is that we want a timeline similar to the attached file, but want to overlay a rising bar chart from left to right that shows the total number of units owned rising through the years. We would like this to be in the background though by using a low opacity value for the color of the graph. A great example of what we want the timeline to look like is at the bottom of the following webpage (we would just need to add the rising bar chart in the background). https://www.tollmeridecap.com/firm. This timeline is what would take the place of page 4 of the attached PP presentation.

In addition to our company landing page, the following website is representative of a style we like: https://www.vak.com

```html
<!DOCTYPE html>
<html lang="en">
<head>
<meta charset="utf-8">
<title>The Quillmark Group — Onboarding Deck</title>
<link href="https://fonts.googleapis.com/css2?family=Roboto:wght@300;400;500;700;900&family=Roboto+Condensed:wght@400;700&display=swap" rel="stylesheet">
<style>
:root{
  --red:#c8202f;
  --red-deep:#981521;
  --red-soft:#e4606a;
  --pink:#f9e6e7;
  --ink:#3a3a3a;
  --grey:#6d6d6d;
  --grey-mid:#b4b4b4;
  --grey-band:#ececec;
  --ph:#efefef;
  --canvas:#dcdcdc;
  --white:#fff;
}
*{box-sizing:border-box;margin:0;padding:0}
html,body{width:1200px;height:2403px;overflow:hidden}
body{background:var(--canvas);font-family:"Roboto",Arial,sans-serif;color:var(--ink);position:relative}
.slide{position:absolute;width:451px;height:252px;background:var(--white);box-shadow:0 4px 10px rgba(0,0,0,.22);overflow:hidden}
.abs{position:absolute}

/* headers */
.kicker{position:absolute;left:12px;top:8px;font:400 14px/1 "Roboto Condensed",Arial,sans-serif;color:var(--ink);letter-spacing:.3px}
.title-box{position:absolute;left:12px;top:22px;background:var(--red);color:var(--white);font:700 19px/1 "Roboto Condensed",Arial,sans-serif;padding:2px 4px 1px;letter-spacing:.3px}
.rule{position:absolute;left:0;right:0;top:50px;height:1px;background:#e2e2e2}

/* footer */
.brand{position:absolute;left:24px;bottom:5px;font:400 9.5px/1 "Roboto",Arial,sans-serif;color:var(--ink)}
.url-tag{position:absolute;right:21px;bottom:0;width:53px;height:14px;background:var(--red-soft);color:#fff;font:400 4px/14px "Roboto",Arial,sans-serif;text-align:center}
.page-no{position:absolute;right:0;bottom:0;width:21px;height:14px;background:var(--red);color:#fff;font:500 5px/14px "Roboto",Arial,sans-serif;text-align:center}

/* timeline */
.band{position:absolute;left:0;right:0;top:132px;height:25px;background:var(--grey-band)}
.timeline{position:absolute;left:12px;right:10px;top:136px;height:17px;display:flex;gap:1px}
.yr{flex:1;background:var(--grey-mid);color:#fff;font:500 7px/17px "Roboto",Arial,sans-serif;text-align:center;clip-path:polygon(0 0,86% 0,100% 50%,86% 100%,0 100%,12% 50%)}
.yr:first-child{clip-path:polygon(0 0,86% 0,100% 50%,86% 100%,0 100%)}
.yr.on{background:var(--red)}
.yr.hot{background:var(--red-deep)}
.pin{position:absolute;width:7px;height:7px;border:1.6px solid var(--red);border-radius:50%;background:#fff}
.pin::after{content:"";position:absolute;left:1.2px;width:1px;height:5px;background:var(--red)}
.pin.up::after{top:5px}
.pin.down::after{bottom:5px}

.ph{position:absolute;background:var(--ph);color:var(--grey);font:400 7px/1 "Roboto",Arial,sans-serif;display:flex;align-items:center;justify-content:center}
.entry{position:absolute;font:400 5px/1.25 "Roboto",Arial,sans-serif;color:var(--ink)}
.entry h4{color:var(--red);font:700 6.2px/1.2 "Roboto",Arial,sans-serif;margin-bottom:1px}
.entry.right{text-align:right}
.entry b{font-weight:700}

/* hero */
.hero{position:absolute;left:257px;top:40px;width:726px;height:409px;background:#fff;box-shadow:0 5px 12px rgba(0,0,0,.25);overflow:hidden}
.hero-photo{position:absolute;left:0;top:0;width:726px;height:327px;background:linear-gradient(120deg,#e9ecef 0%,#d8d4cd 45%,#bfb9ad 62%,#8e8f74 80%,#c9cdd2 100%)}
.hero-veil{position:absolute;left:28px;top:28px;width:263px;height:306px;background:rgba(255,255,255,.72)}
.hero-sq{position:absolute;top:0;width:28px;height:28px;background:var(--red)}
.hero-strip{position:absolute;left:28px;top:0;width:263px;height:28px;background:#f3d3d5}
.hero-foot{position:absolute;left:0;top:327px;width:313px;height:82px;background:var(--red)}
.hero-dash{position:absolute;left:40px;top:92px;width:33px;height:4px;background:var(--red)}
.hero-title{position:absolute;left:40px;top:106px;font:700 27.5px/1.08 "Roboto",Arial,sans-serif;color:var(--ink);letter-spacing:.2px}
.hero-title .hl{color:var(--red)}
.hero-brand{position:absolute;left:313px;top:327px;width:413px;height:82px;display:flex;align-items:center;justify-content:center;font:400 29px/1 "Roboto",Arial,sans-serif;color:#222}

/* who we are */
.who-photo{position:absolute;left:0;top:0;width:194px;height:236px;background:linear-gradient(160deg,#5b7fb0 0%,#9fb6d3 35%,#e6e6e6 60%,#8a8a8a 100%)}
.who-body{position:absolute;left:205px;top:52px;width:230px;font:400 5px/1.3 "Roboto",Arial,sans-serif;color:var(--ink)}
.who-body ul{list-style:none;margin-top:3px}
.who-body li{position:relative;padding-left:10px;margin-bottom:4px}
.who-body li::before{content:"";position:absolute;left:0;top:1px;width:5px;height:5px;border-radius:50%;background:var(--ink)}
.who-body li b{color:var(--red);font-weight:700}

/* business lines */
.bl-photo{position:absolute;left:0;top:0;width:451px;height:107px;background:linear-gradient(90deg,#4c5562 0%,#6f7884 50%,#434b57 100%)}
.bl-card{position:absolute;top:87px;width:119px;height:30px;background:#fff;box-shadow:0 1px 3px rgba(0,0,0,.2);border-bottom:2px solid var(--red);display:flex;align-items:center;justify-content:center;font:500 11px/1 "Roboto",Arial,sans-serif;color:var(--ink)}
.bl-text{position:absolute;top:124px;width:120px;font:400 4.4px/1.3 "Roboto",Arial,sans-serif;color:var(--grey)}

/* stats */
.tile{position:absolute;width:128px;height:81px;background:#fff;border:1px solid #ececec;text-align:center}
.tile-head{height:27px;display:flex;align-items:center;justify-content:center}
.tile-head.red{background:var(--red)}
.tile-head.grey{background:#8c8c8c}
.tile-label{font:400 7.6px/1.2 "Roboto",Arial,sans-serif;color:var(--ink);margin-top:5px}
.tile-val{font:300 16px/1 "Roboto",Arial,sans-serif;margin-top:4px}
.val-red{color:var(--red)}
.val-grey{color:var(--ink)}
.stat{position:absolute;width:120px;font:400 7.6px/1.2 "Roboto",Arial,sans-serif;color:var(--ink)}
.stat .tile-val{margin-top:3px;font-size:16px}
.stat.right{text-align:right}
.stat-rule{width:18px;height:1px;background:#bbb;margin-top:7px}
.stat.right .stat-rule{margin-left:auto}

/* portfolio */
.map{position:absolute;left:24px;top:62px;width:266px;height:158px;background:linear-gradient(135deg,#d0d0d0 0%,#c8202f 45%,#d0d0d0 70%,#c8202f 100%);opacity:.85;border-radius:4px}
.pf-panel{position:absolute;left:296px;top:0;width:155px;height:236px;background:var(--pink)}
.pf-head{position:absolute;left:17px;top:56px;font:400 10.5px/1.2 "Roboto",Arial,sans-serif;color:var(--red)}
.pf-text{position:absolute;left:17px;top:90px;width:125px;font:400 7.2px/1.25 "Roboto",Arial,sans-serif;color:var(--ink)}
.pf-text ul{list-style:none;margin-top:3px}
.pf-text li{position:relative;padding-left:6px;margin-bottom:2px}
.pf-text li::before{content:"•";position:absolute;left:0}

/* tomorrow */
.tm-col{position:absolute;top:62px;width:63px;height:140px;background:var(--red);color:#fff;text-align:center;padding:6px 3px;font:400 4.4px/1.25 "Roboto",Arial,sans-serif}
.tm-col.deep{background:var(--red-deep)}
.tm-col b{display:block;font-weight:700;font-size:5px;margin:3px 0 1px}
.tm-line{position:absolute;left:24px;right:24px;top:218px;height:1px;background:#d6d6d6}
.tm-dot{position:absolute;top:214px;width:8px;height:8px;border-radius:50%;background:var(--red);border:1.5px solid #fff;box-shadow:0 0 0 1px var(--red)}
</style>
</head>
<body>

<!-- Cover -->
<section class="hero">
  <div class="hero-photo" role="img" aria-label="Photo of a modern white apartment building with balconies and trees"></div>
  <div class="hero-veil"></div>
  <div class="hero-sq" style="left:0"></div>
  <div class="hero-strip"></div>
  <div class="hero-sq" style="left:291px;width:22px"></div>
  <div class="hero-foot"></div>
  <div class="hero-dash"></div>
  <h1 class="hero-title">PROVIDING<br>INNOVATIVE<br>HOUSING<br><span class="hl">SOLUTIONS<br>NATIONWIDE.</span></h1>
  <div class="hero-brand">The Quillmark Group</div>
</section>

<!-- 2 Who we are -->
<section class="slide" style="left:129px;top:503px">
  <div class="who-photo" role="img" aria-label="Upward view of a modern apartment tower facade"></div>
  <div class="kicker" style="left:205px">WHO</div>
  <div class="title-box" style="left:205px">WE ARE</div>
  <div class="who-body">
    <p>The Quillmark Group develops and invests nationally in quality real estate projects across multiple business lines. We approach business through an entrepreneurial lens, cultivating a team who acts entrepreneurially and rewards team members commensurate with their contributions. This approach drives us to produce outsized returns.</p>
    <p style="margin-top:4px">While what we do determines our day-to-day, it's what we believe that makes us The Quillmark Group.</p>
    <ul>
      <li><b>We believe in being action oriented.</b> Results are achieved by compressing the distance between good ideas and great execution.</li>
      <li><b>We believe in authenticity.</b> It doesn't take a suit and tie to solve big problems. Work hard and be yourself.</li>
      <li><b>We believe in big goals.</b> In order to achieve uncommon results, our goals must push us out of our comfort zone, beyond what we think is possible.</li>
      <li><b>We believe we can do well while doing good.</b> We give back to our communities and aim to have a lasting social impact.</li>
      <li><b>We believe work and fun are not mutually exclusive.</b> When done right, hard work can be a lot of fun.</li>
      <li><b>We believe in a thoughtful approach.</b> We utilize our experience and a considered approach to make swift, reasoned and forward-thinking decisions.</li>
    </ul>
  </div>
  <div class="brand">The Quillmark Group</div>
  <div class="url-tag">www.thequillmrk.com</div><div class="page-no">2</div>
</section>

<!-- 3 Business lines -->
<section class="slide" style="left:620px;top:630px">
  <div class="bl-photo" role="img" aria-label="Low-angle photo of apartment buildings against a grey sky"></div>
  <div class="kicker" style="left:0;width:451px;text-align:center;top:22px;color:#fff">OUR</div>
  <div class="title-box" style="left:144px;top:36px">BUSINESS LINES</div>
  <div class="bl-card" style="left:24px">Quillmark Capital</div>
  <div class="bl-card" style="left:166px">Quillmark Communities</div>
  <div class="bl-card" style="left:308px">Quillmark Impact</div>
  <p class="bl-text" style="left:24px">Quillmark Capital is the Group's market rate investment vehicle founded on the basis of value investing philosophies, focusing on distressed, opportunistic, value-add and niche market real estate assets. Within these classes, it typically targets underperforming properties that often require significant renovations and hands-on management to realize the assets' full potential. It constantly assesses market conditions and end-user demand in order to identify short- and long-term inefficiencies and arbitrage opportunities, applying a methodical approach to set the stage for superior returns.</p>
  <p class="bl-text" style="left:166px">In the context of a deepening affordability crisis, the Group entered affordable housing in 2013 with the establishment of Quillmark Communities, a developer, owner, and operator focused on providing affordable housing nationwide. Through property-based Section 8 subsidies, Low Income Housing Tax Credits, and additional programs, it aims to preserve and expand long term housing affordability for low-income households. The team has a proven track record in safeguarding and growing the number of affordable units throughout the country.</p>
  <p class="bl-text" style="left:308px">Quillmark Impact Housing was founded to address the housing problem for middle income earners — moderate-income individuals that cannot afford to reside in the communities in which they work. Drawing upon the company's affordable and market-rate housing expertise, it creates quality, income restricted housing units. These serve middle-income residents who earn in excess of traditional affordable limits yet cannot afford market rate housing. The company pursues these projects through strategic public-private partnerships with government agencies and financial institutions.</p>
  <div class="brand">The Quillmark Group</div>
  <div class="url-tag">www.thequillmrk.com</div><div class="page-no">3</div>
</section>

<!-- 4 History 2010 -->
<section class="slide" style="left:129px;top:796px">
  <div class="kicker">COMPANY</div><div class="title-box">HISTORY</div><div class="rule"></div>
  <div class="entry" style="left:24px;top:59px;width:262px">
    <h4>What do you get when you combine a principal, an unpaid intern, and 5,000 square feet of borrowed office space? The beginning of Quillmark</h4>
    In 2010, we founded the Company based on value investing principals in the depths of the Great Financial Crisis with a focus on value-add, distressed and opportunistic investments. We leverage our significant experience and track record in the value-add institutional real estate investment space, starting small and building an investment firm from the ground up. It may not be the easiest path to choose, but <b><i>we do what's right and not what's easy.</i></b>
  </div>
  <div class="ph" style="left:296px;top:58px;width:82px;height:57px">[ Image ]</div>
  <div class="pin up" style="left:23px;top:122px"></div>
  <div class="band"></div>
  <div class="timeline"><div class="yr on">2010</div><div class="yr">2011</div><div class="yr">2012</div><div class="yr">2013</div><div class="yr">2014</div><div class="yr">2015</div><div class="yr">2016</div><div class="yr">2017</div><div class="yr">2018</div><div class="yr">2019</div><div class="yr">2020</div><div class="yr">2021</div><div class="yr">2022</div></div>
  <div class="pin down" style="left:23px;top:164px"></div>
  <div class="entry" style="left:24px;top:176px;width:262px">
    <h4>Start with what you know</h4>
    Finding a hidden gem, polishing it, and presenting it to the world can be a lot of fun. We know how to do it and enjoy doing it, so we decide to dive into the value-add apartment business. We find the worn out properties in great neighborhoods and we find the underutilized properties in the next hot neighborhoods. The key to success is to see things for what they can be, and not just what they are, then to <b><i>innovate through reimaging, reorganizing and reworking.</i></b>
  </div>
  <div class="ph" style="left:296px;top:172px;width:82px;height:54px">[ Image ]</div>
  <div class="brand">The Quillmark Group</div>
  <div class="url-tag">www.thequillmrk.com</div><div class="page-no">4</div>
</section>

<!-- 5 History 2011 -->
<section class="slide" style="left:620px;top:923px">
  <div class="kicker">COMPANY</div><div class="title-box">HISTORY</div><div class="rule"></div>
  <div class="entry" style="left:20px;top:59px;width:305px">
    <h4>Who wouldn't want to buy $1.00 for 70 cents?</h4>
    Armed with a man at the court house steps with an earpod in one ear and millions of dollars of cashiers checks in his back pocket, we embark on a daily ritual of bidding on apartment building foreclosures. Through the Harbor Lane Fund, a discretionary investment fund we raise to bid on foreclosed, distressed apartments, we successfully invest in this space over a four year period. With no traditional diligence available for the properties, and just seconds to bid, it can be a nerve wracking experience, but we never lose money on any of the acquisitions, and actually earn quite an attractive return. If this isn't a crash course in making swift, reasoned, and forward thinking decisions, we don't know what is.
  </div>
  <div class="ph" style="left:333px;top:59px;width:82px;height:56px">[ Image ]</div>
  <div class="pin up" style="left:57px;top:122px"></div>
  <div class="band"></div>
  <div class="timeline"><div class="yr">2010</div><div class="yr hot">2011</div><div class="yr">2012</div><div class="yr">2013</div><div class="yr">2014</div><div class="yr">2015</div><div class="yr">2016</div><div class="yr">2017</div><div class="yr">2018</div><div class="yr">2019</div><div class="yr">2020</div><div class="yr">2021</div><div class="yr">2022</div></div>
  <div class="brand">The Quillmark Group</div>
  <div class="url-tag">www.thequillmrk.com</div><div class="page-no">5</div>
</section>

<!-- 6 History 2012-2013 -->
<section class="slide" style="left:129px;top:1089px">
  <div class="kicker">COMPANY</div><div class="title-box">HISTORY</div><div class="rule"></div>
  <div class="ph" style="left:22px;top:58px;width:82px;height:57px">[ Image ]</div>
  <div class="entry" style="left:112px;top:80px;width:310px">
    <h4>Eureka!</h4>
    After a nail biting 22 months of money going out the door during the Company's initial existence, we successfully complete our first disposition of an investment which (thankfully) brings some profit back into the bank account. With a sale price 55% above our purchase, we're off to a good start. And better yet, our investment thesis is validated.
  </div>
  <div class="pin up" style="left:112px;top:122px"></div>
  <div class="band"></div>
  <div class="timeline"><div class="yr">2010</div><div class="yr">2011</div><div class="yr on">2012</div><div class="yr hot">2013</div><div class="yr">2014</div><div class="yr">2015</div><div class="yr">2016</div><div class="yr">2017</div><div class="yr">2018</div><div class="yr">2019</div><div class="yr">2020</div><div class="yr">2021</div><div class="yr">2022</div></div>
  <div class="pin down" style="left:112px;top:164px"></div>
  <div class="ph" style="left:22px;top:172px;width:82px;height:54px">[ Image ]</div>
  <div class="entry" style="left:112px;top:176px;width:320px">
    <h4>Doing well while doing good.</h4>
    After rigorous analysis we dip our toe in the affordable housing waters because of perceived opportunity. While the initial opportunity is just a sliver of the vast affordable housing landscape we uncover in the years to come, the affordable housing industry becomes more of a mission rather than just a mere opportunity. We create a new segment of the business, Quillmark Communities, to focus on fulfilling affordable housing needs across the country. This would not be possible without our <b>pursuit of lifelong learning</b>, allowing us to marry our existing multifamily experience with a new asset class.
  </div>
  <div class="brand">The Quillmark Group</div>
  <div class="url-tag">www.thequillmrk.com</div><div class="page-no">6</div>
</section>

<!-- 7 History 2015-2017 -->
<section class="slide" style="left:620px;top:1216px">
  <div class="kicker">COMPANY</div><div class="title-box">HISTORY</div><div class="rule"></div>
  <div class="ph" style="left:131px;top:58px;width:82px;height:57px">[ Image ]</div>
  <div class="entry" style="left:222px;top:82px;width:210px">
    <h4>Ladies and gentlemen, start your engines.</h4>
    While the debate still rages in the office as to who actually won the inaugural Quillmark go karting race, one thing is certain: we all walk away that day with big smiles on our faces. <b>We work hard and have fun</b>, otherwise, what's the point?
  </div>
  <div class="pin up" style="left:222px;top:122px"></div>
  <div class="band"></div>
  <div class="timeline"><div class="yr">2010</div><div class="yr">2011</div><div class="yr">2012</div><div class="yr">2013</div><div class="yr">2014</div><div class="yr hot">2015</div><div class="yr on">2016</div><div class="yr hot">2017</div><div class="yr">2018</div><div class="yr">2019</div><div class="yr">2020</div><div class="yr">2021</div><div class="yr">2022</div></div>
  <div class="pin down" style="left:222px;top:164px"></div>
  <div class="ph" style="left:48px;top:174px;width:82px;height:54px">[ Image ]</div>
  <div class="entry" style="left:112px;top:172px;width:322px">
    <h4>The Naked City</h4>
    Just off the glittering Las Vegas strip we find what we believe to be an attractive affordable housing opportunity. But once we complete our diligence, we realize that the property has too many physical needs to be a viable long term investment. Rather than walking away, we decide to dive deeper into the affordable housing world by utilizing the Low Income Housing Tax Credit to complete a redevelopment of the 201 unit property located in a neighborhood known as The Naked City for its history as a home to many of Las Vegas' showgirls in the 50's and 60's. This redevelopment not only enhances the lives of the property's residents, but contributes to lifting the entire neighborhood. This is the first of many projects Quillmark Communities undertakes to redevelop affordable housing across the country.
  </div>
  <div class="brand">The Quillmark Group</div>
  <div class="url-tag">www.thequillmrk.com</div><div class="page-no">7</div>
</section>

<!-- 8 History 2019-2021 -->
<section class="slide" style="left:129px;top:1382px">
  <div class="kicker">COMPANY</div><div class="title-box">HISTORY</div><div class="rule"></div>
  <div class="entry right" style="left:70px;top:60px;width:270px">
    <h4>46..., 47..., 48...., 49...., 50!</h4>
    Never are we met with such a range of emotions for a company activity: excitement, nervousness, dread. The Quillmark health challenge is a 60 day competition that tests our willpower, establishes beneficial habits, and leaves us feeling a better version of ourselves. We gain points by simply eating right and working out, all while having a trainer cheering us along or giving us a nudge. Our single biggest competitor is ourself. To be successful, <b>we must approach each day with intention</b>, just like we approach our business. A testament to the spirit of the team, the competition is neck and neck until the very end.
  </div>
  <div class="ph" style="left:347px;top:58px;width:82px;height:57px">[ Image ]</div>
  <div class="pin up" style="left:335px;top:122px"></div>
  <div class="band"></div>
  <div class="timeline"><div class="yr">2010</div><div class="yr">2011</div><div class="yr">2012</div><div class="yr">2013</div><div class="yr">2014</div><div class="yr">2015</div><div class="yr">2016</div><div class="yr">2017</div><div class="yr">2018</div><div class="yr hot">2019</div><div class="yr on">2020</div><div class="yr hot">2021</div><div class="yr">2022</div></div>
  <div class="pin down" style="left:335px;top:164px"></div>
  <div class="entry right" style="left:30px;top:176px;width:310px">
    <h4>Solving for the missing middle</h4>
    How can we have thriving cities when the people who work and play there cannot afford to live there? Spoiler alert: we can't. Expensive, high-end housing pencils to build. Affordable housing for low income renters, although scarce, can pencil to build through government funded programs. But what about middle income renters who make the cities run? They are left with dilapidated, old housing stock, or spending hours a day fighting traffic to get to and from work. <b>Harnessing the collective and collaborative power of a public/private team</b>, Quillmark Impact Housing is born to address this crucial need, providing high quality housing to the teachers, nurses, and numerous professionals who are the life blood of our cities.
  </div>
  <div class="ph" style="left:347px;top:172px;width:82px;height:54px">[ Image ]</div>
  <div class="brand">The Quillmark Group</div>
  <div class="url-tag">www.thequillmrk.com</div><div class="page-no">8</div>
</section>

<!-- 9 History 2021-2022 -->
<section class="slide" style="left:620px;top:1509px">
  <div class="kicker">COMPANY</div><div class="title-box">HISTORY</div><div class="rule"></div>
  <div class="ph" style="left:48px;top:58px;width:82px;height:57px">[ Image ]</div>
  <div class="entry right" style="left:140px;top:70px;width:270px">
    <h4>Don't step in the kitchen</h4>
    What company retreat is complete without a bit of work, a lot of laughs, and little competition? The competitive juices are in full swing at the first Quillmark pickleball tournament. The open courtside bar soothes the sting of defeat, but regardless of where we each rank in the standings, there is a lot of talk of pickleball becoming the new favorite Quillmark pastime.
  </div>
  <div class="pin up" style="left:405px;top:122px"></div>
  <div class="band"></div>
  <div class="timeline"><div class="yr">2010</div><div class="yr">2011</div><div class="yr">2012</div><div class="yr">2013</div><div class="yr">2014</div><div class="yr">2015</div><div class="yr">2016</div><div class="yr">2017</div><div class="yr">2018</div><div class="yr">2019</div><div class="yr">2020</div><div class="yr hot">2021</div><div class="yr on">2022</div></div>
  <div class="pin down" style="left:405px;top:164px"></div>
  <div class="ph" style="left:48px;top:172px;width:82px;height:54px">[ Image ]</div>
  <div class="entry right" style="left:140px;top:180px;width:270px">
    <h4>Movin' on up</h4>
    The growth and success of a company does not happen overnight, nor does it just happen. It takes a team of dedicated, intelligent, results oriented individuals to deliver exceptional results. When a member of the team consistently delivers results, <b>we reward those results</b>. In this case, we name our first Partner.
  </div>
  <div class="brand">The Quillmark Group</div>
  <div class="url-tag">www.thequillmrk.com</div><div class="page-no">9</div>
</section>

<!-- 10 Where we are now: tiles -->
<section class="slide" style="left:129px;top:1675px">
  <div class="kicker" style="left:24px">WHERE</div><div class="title-box" style="left:24px">ARE WE NOW</div>
  <div class="tile" style="left:24px;top:54px">
    <div class="tile-head red"><svg width="16" height="14" viewBox="0 0 16 14" fill="#fff"><rect x="1" y="5" width="5" height="9"/><rect x="7" y="1" width="8" height="13"/></svg></div>
    <div class="tile-label">Apartment Units<br>Acquired</div><div class="tile-val val-red">7,500 +</div>
  </div>
  <div class="tile" style="left:162px;top:54px">
    <div class="tile-head grey"><svg width="20" height="12" viewBox="0 0 20 12" fill="#fff"><circle cx="10" cy="3" r="2.6"/><circle cx="4" cy="4" r="2"/><circle cx="16" cy="4" r="2"/><path d="M5 12a5 4 0 0 1 10 0z"/><path d="M0 12a4 3 0 0 1 7-2v2zM20 12a4 3 0 0 0-7-2v2z"/></svg></div>
    <div class="tile-label">Senior Management Team<br>Acquisition Experience</div><div class="tile-val val-grey">Over $4 billion</div>
  </div>
  <div class="tile" style="left:302px;top:54px">
    <div class="tile-head red"><svg width="12" height="14" viewBox="0 0 12 14" fill="none" stroke="#fff" stroke-width="1.3"><rect x="1" y="1" width="10" height="12"/><path d="M3 5h6M3 8h6M3 11h4"/></svg></div>
    <div class="tile-label">Current Assets<br>Under Management</div><div class="tile-val val-red">$1+ billion</div>
  </div>
  <div class="tile" style="left:24px;top:145px">
    <div class="tile-head grey"><svg width="18" height="12" viewBox="0 0 18 12" fill="none" stroke="#fff" stroke-width="1.4"><path d="M1 2h16M2 2v10M6 2v10M10 2v10M14 2v10M1 6h16"/></svg></div>
    <div class="tile-label">Number of<br>Residents Served</div><div class="tile-val val-grey">13,000+</div>
  </div>
  <div class="tile" style="left:162px;top:145px">
    <div class="tile-head red"><svg width="14" height="14" viewBox="0 0 14 14" fill="#fff"><path d="M3 6a4 4 0 0 1 8 0z"/><rect x="2" y="6" width="10" height="1.2"/><path d="M2 14a5 5 0 0 1 10 0z"/></svg></div>
    <div class="tile-label">Renovations<br>Performed</div><div class="tile-val val-red">$60mm+</div>
  </div>
  <div class="tile" style="left:302px;top:145px">
    <div class="tile-head grey"><svg width="16" height="12" viewBox="0 0 16 12" fill="none" stroke="#fff" stroke-width="1.4"><path d="M1 1v10h14M3 8l4-4 3 2 4-4"/></svg></div>
    <div class="tile-label">IRR of Realized Investments<br>– Quillmark Communities</div><div class="tile-val val-grey">34.87%</div>
  </div>
  <div class="brand">The Quillmark Group</div>
  <div class="url-tag">www.thequillmrk.com</div><div class="page-no">10</div>
</section>

<!-- 11 Where we are now: donut -->
<section class="slide" style="left:620px;top:1802px">
  <div class="kicker" style="left:24px">WHERE</div><div class="title-box" style="left:24px">ARE WE NOW</div>
  <div class="stat right" style="left:10px;top:58px">Number of<br>Residents Served<div class="tile-val val-grey">13,000+</div><div class="stat-rule"></div></div>
  <div class="stat right" style="left:10px;top:122px">Renovations<br>Performed<div class="tile-val val-red">$60mm+</div><div class="stat-rule"></div></div>
  <div class="stat right" style="left:10px;top:186px">IRR of Realized Investments<br>– Quillmark Communities<div class="tile-val val-grey">34.87%</div></div>
  <div class="stat" style="left:322px;top:58px">Apartment Units<br>Acquired<div class="tile-val val-red">7,500 +</div><div class="stat-rule"></div></div>
  <div class="stat" style="left:322px;top:122px">Senior Management Team<br>Acquisition Experience<div class="tile-val val-grey">Over $4 billion</div><div class="stat-rule"></div></div>
  <div class="stat" style="left:322px;top:186px">Current Assets<br>Under Management<div class="tile-val val-red">$1+ billion</div></div>
  <svg class="abs" style="left:155px;top:94px" width="140" height="140" viewBox="0 0 140 140">
    <g fill="none" stroke-width="32">
      <circle cx="70" cy="70" r="54" stroke="#a91c28" stroke-dasharray="54.5 284.8" transform="rotate(-90 70 70)"/>
      <circle cx="70" cy="70" r="54" stroke="#8c1520" stroke-dasharray="54.5 284.8" transform="rotate(-30 70 70)"/>
      <circle cx="70" cy="70" r="54" stroke="#a91c28" stroke-dasharray="54.5 284.8" transform="rotate(30 70 70)"/>
      <circle cx="70" cy="70" r="54" stroke="#8c1520" stroke-dasharray="54.5 284.8" transform="rotate(90 70 70)"/>
      <circle cx="70" cy="70" r="54" stroke="#a91c28" stroke-dasharray="54.5 284.8" transform="rotate(150 70 70)"/>
      <circle cx="70" cy="70" r="54" stroke="#8c1520" stroke-dasharray="54.5 284.8" transform="rotate(210 70 70)"/>
    </g>
    <g fill="#fff">
      <rect x="93" y="28" width="4" height="8"/><rect x="98" y="24" width="6" height="12"/>
      <circle cx="122" cy="68" r="2.5"/><path d="M116 76a6 4 0 0 1 12 0z"/>
      <rect x="92" y="104" width="8" height="10" fill="none" stroke="#fff" stroke-width="1.2"/>
      <path d="M38 106v9h11M40 113l3-3 3 2 3-4" fill="none" stroke="#fff" stroke-width="1.2"/>
      <path d="M14 68a4 4 0 0 1 8 0z"/><path d="M13 77a5 4 0 0 1 10 0z"/>
      <path d="M36 28h12M37 28v8M41 28v8M45 28v8" fill="none" stroke="#fff" stroke-width="1.2"/>
    </g>
  </svg>
  <div class="brand">The Quillmark Group</div>
  <div class="url-tag">www.thequillmrk.com</div><div class="page-no">11</div>
</section>

<!-- 12 Portfolio -->
<section class="slide" style="left:129px;top:1968px">
  <div class="pf-panel"></div>
  <div class="kicker" style="left:24px">OUR</div><div class="title-box" style="left:24px">NATIONWIDE PORTFOLIO</div>
  <div class="map" role="img" aria-label="Map of the United States with portfolio states highlighted in red"></div>
  <div class="pf-head" style="left:313px">HEADING<br>TEXT HERE</div>
  <div class="pf-text" style="left:313px">
    Lorem ipsum dolor sit amet, ullum corpora delicata duo. Rebum insolens pri eu. No alia tota modus qui.
    <ul>
      <li>Sint brute at usu. Duo iisque appareat adversarium at.</li>
      <li>Sint brute at usu. Duo iisque appareat adversarium at.</li>
      <li>Sint brute at usu. Duo iisque appareat adversarium at.</li>
    </ul>
  </div>
  <div class="brand">The Quillmark Group</div>
  <div class="url-tag">www.thequillmrk.com</div><div class="page-no">12</div>
</section>

<!-- 13 Tomorrow -->
<section class="slide" style="left:620px;top:2095px">
  <div class="kicker" style="left:24px">WHAT DOES</div><div class="title-box" style="left:24px">TOMORROW LOOK LIKE?</div>
  <div class="tm-col" style="left:24px"><svg width="14" height="12" viewBox="0 0 14 12" fill="none" stroke="#fff"><circle cx="7" cy="3" r="2"/><path d="M2 11a5 4 0 0 1 10 0"/></svg><b>We will be a market leader.</b>We will pursue growth and innovation to achieve industry beating returns and exponentially expand our portfolio through new and existing business lines.</div>
  <div class="tm-col" style="left:92px"><svg width="14" height="12" viewBox="0 0 14 12" fill="none" stroke="#fff"><path d="M7 1v10M3 5l4-4 4 4"/></svg><b>We will positively impact those we touch.</b>We have a responsibility to create opportunity for our residents and our employees. Investing in the success of both parties, particularly by empowering individuals, will help us enact the social impact that is sorely needed.</div>
  <div class="tm-col" style="left:160px"><svg width="14" height="12" viewBox="0 0 14 12" fill="none" stroke="#fff"><circle cx="7" cy="5" r="4"/><path d="M5 11h4"/></svg><b>We will have a positive impact on those we touch.</b>We will positively impact all stakeholders in our business (residents, employees, communities and investors) by adhering to a high standard in terms of both our fiduciary and social obligations.</div>
  <div class="tm-col deep" style="left:228px"><svg width="14" height="12" viewBox="0 0 14 12" fill="none" stroke="#fff"><circle cx="4" cy="4" r="2"/><circle cx="10" cy="4" r="2"/><path d="M1 11h12"/></svg><b style="font-weight:400">We will have a positive and lasting effect on residents and communities by doing what's right not what's easy.</b></div>
  <div class="tm-col" style="left:296px"><svg width="14" height="12" viewBox="0 0 14 12" fill="none" stroke="#fff"><path d="M2 2l4 4M12 2l-4 4M2 10l4-4M12 10l-4-4"/></svg><b>We will reduce our footprint.</b>We recognize that the construction industry has a significant carbon footprint. Through our perpetual desire to innovate through reimagining, reorganizing and reworking, we will find further solutions to substantially reduce the carbon footprint of our communities.</div>
  <div class="tm-col" style="left:364px"><svg width="14" height="12" viewBox="0 0 14 12" fill="none" stroke="#fff"><circle cx="7" cy="4" r="3"/><path d="M3 11h8"/></svg><b>We will utilize our expertise to its fullest.</b>The multifamily industry has been one of the highest performing asset classes, and is poised to remain such. We will outperform the already favorable market by applying all of our experience to mitigate risk and enhance upside.</div>
  <div class="tm-line"></div>
  <div class="tm-dot" style="left:52px"></div>
  <div class="tm-dot" style="left:120px"></div>
  <div class="tm-dot" style="left:188px"></div>
  <div class="tm-dot" style="left:256px"></div>
  <div class="tm-dot" style="left:324px"></div>
  <div class="tm-dot" style="left:392px"></div>
  <div class="brand">The Quillmark Group</div>
  <div class="url-tag">www.thequillmrk.com</div><div class="page-no">13</div>
</section>

</body>
</html>
```